Lumen Gathering 2019 Enemies of the End-Times Church Flyer

We want a church conference flyer designed. We are looking for a professional, yet catchy design that uses our brand colors and logo creatively while communicating key information of the event effectively. <br/>The flyer must include all of the following:<br/>Title: Lumen Gathering 2019<br/>Topic: The Enemies of The End-Times Church <br/>Subtitles: <br/> -How the antichrist raises an army by social behavior engineering. <br/>-How the architects of modern social constructs escaped the church's radar. <br/>-The Holy Spirit's end-times agenda:<br/> The Knock-Out Punch!<br/>Speaker: Prophet Marcus Obuya <br/>Dates/time: December 27, 28 & 29 at 6pm<br/>Location: Thistle Community Center <br/> 412 Farrow Lane <br/> Portland, ME 04219<br/>Contact info: phone: 207-583-1924 <br/>email: contact@vellorbrook.org <br/> www.toskin.org<br/>*The flyer must also include a picture of the speaker and our Toskin logo <br/>Thanks, we look forward to seeing what you come up with!

Colors

Designer to choose colors to be used in the design.

Requirements
Must have
• The flyer must include all of the following:
• Title: Lumen Gathering 2019
• Topic: The Enemies of The End-Times Church
• Subtitles:
• -How the antichrist raises an army by social behavior engineering.
• -How the architects of modern social constructs escaped the church's radar.
• -The Holy Spirit's end-times agenda:
• The Knock-Out Punch!
• Speaker: Prophet Marcus Obuya
• Dates/time: December 27, 28 & 29 at 6pm
• Location: Thistle Community Center
• 412 Farrow Lane
• Portland, ME 04219
• Contact info: phone: 207-583-1924
• email: contact@vellorbrook.org
• www.toskin.org
• *The flyer must also include a picture of the speaker and our Toskin logo
Should not have
• Pictures of crosses or church buildings

```html
<!DOCTYPE html>
<html lang="en">
<head>
<meta charset="utf-8">
<title>Lumen Gathering 2019</title>
<link href="https://fonts.googleapis.com/css2?family=Bebas+Neue&family=Roboto:wght@400;500&display=swap" rel="stylesheet">
<style>
  :root {
    --navy: #003a5d;
    --orange: #f5921e;
    --paper: #ebe9ea;
    --ink: #1b1b1b;
    --photo-dark: #2f3236;
    --photo-mid: #4a4d52;
  }
  html, body { margin: 0; padding: 0; overflow: hidden; background: var(--paper); }
  .flyer {
    position: relative; width: 848px; height: 1200px; overflow: hidden;
    background: var(--paper); color: var(--ink);
    font-family: "Roboto", Arial, sans-serif;
  }
  .backdrop { position: absolute; inset: 0; }
  .display { font-family: "Bebas Neue", Impact, sans-serif; line-height: 1; position: absolute; margin: 0; font-weight: 400; }
  .brand { left: 37px; top: 60px; display: flex; align-items: center; gap: 10px; }
  .brand-dot { width: 22px; height: 22px; border-radius: 50%; background: var(--orange); }
  .brand-name { font-family: "Bebas Neue", Impact, sans-serif; font-size: 62px; color: #fff; line-height: 1; position: static; }
  .title { right: 36px; text-align: right; }
  .title-main { top: 77px; font-size: 112px; }
  .title-sub { top: 176px; font-size: 64px; }
  .title-year { top: 232px; font-size: 112px; }
  .topic-label { left: 37px; top: 282px; font-size: 25px; }
  .topic-text { left: 37px; top: 312px; font-size: 26px; }
  .points { position: absolute; left: 37px; top: 380px; width: 400px; margin: 0; padding: 0; list-style: none; }
  .points li {
    position: relative; padding-left: 14px; font-size: 13.4px; font-weight: 500;
    line-height: 23px; margin-bottom: 22px; text-transform: uppercase;
  }
  .points li::before { content: "-"; position: absolute; left: 0; top: 0; }
  .date-month { left: 35px; top: 608px; font-size: 59px; }
  .date-days {
    position: absolute; left: 37px; top: 666px; width: 112px; height: 23px;
    background: var(--ink); color: var(--orange); font-family: "Bebas Neue", Impact, sans-serif;
    font-size: 27px; line-height: 27px; text-align: center; overflow: hidden;
  }
  .date-time { left: 162px; top: 662px; font-size: 32px; }
  .speaker { left: 37px; top: 730px; font-size: 22px; }
  .contact { position: absolute; display: flex; align-items: center; gap: 22px; font-size: 15px; line-height: 24px; color: #222; }
  .contact svg { flex: none; }
  .contact-address { left: 36px; top: 988px; }
  .contact-phone { left: 408px; top: 1008px; font-size: 18px; }
  .contact-email { left: 36px; top: 1090px; gap: 18px; }
  .contact-web { left: 408px; top: 1090px; }
  .rule { position: absolute; left: 36px; top: 1158px; width: 776px; height: 1px; background: var(--ink); }
</style>
</head>
<body>
<main class="flyer">
  <svg class="backdrop" width="848" height="1200" viewBox="0 0 848 1200">
    <polygon points="0,225 157,183 848,413 848,980 0,768" fill="var(--orange)"/>
    <polygon points="0,0 841,0 0,225" fill="var(--navy)"/>
    <polygon points="0,768 848,980 848,1010 0,885" fill="var(--navy)"/>
    <defs>
      <linearGradient id="speakerTone" x1="0" y1="0" x2="0" y2="1">
        <stop offset="0" stop-color="var(--photo-mid)"/>
        <stop offset="1" stop-color="var(--photo-dark)"/>
      </linearGradient>
    </defs>
    <path role="img" aria-label="Portrait photo of the speaker, Prophet Marcus Obuya"
      d="M525 242 C590 238 625 290 622 360 C620 420 600 470 610 500 C680 520 770 520 790 560 C815 640 812 780 800 900 L770 980 L340 860 C345 760 380 640 430 560 C460 520 500 500 490 470 C450 420 440 340 460 290 C475 258 500 244 525 242 Z"
      fill="url(#speakerTone)"/>
  </svg>

  <div class="display brand"><span class="brand-dot"></span><span class="brand-name">TOSKIN</span></div>

  <h1 class="display title title-main">LUMEN</h1>
  <p class="display title title-sub">GATHERING</p>
  <p class="display title title-year">2019</p>

  <p class="display topic-label">TOPIC :</p>
  <h2 class="display topic-text">THE ENEMIES OF THE END-TIMES CHURCH</h2>

  <ul class="points">
    <li>How the antichrist raises an army by social behavior engineering.</li>
    <li>How the architects of modern social constructs escaped the church's radar.</li>
    <li>The Holy Spirit's end-times agenda:</li>
    <li>The knock-out punch!</li>
  </ul>

  <p class="display date-month">DECEMBER</p>
  <div class="date-days">27, 28 &amp; 29</div>
  <p class="display date-time">AT 6PM</p>

  <p class="display speaker">SPEAKER :&nbsp; PROPHET MARCUS OBUYA</p>

  <div class="contact contact-address">
    <svg width="32" height="32" viewBox="0 0 32 32" aria-hidden="true"><circle cx="16" cy="16" r="16" fill="var(--navy)"/><path d="M16 7c-3.6 0-6 2.6-6 5.8 0 4.2 6 11.2 6 11.2s6-7 6-11.2C22 9.6 19.6 7 16 7zm0 8.3a2.4 2.4 0 1 1 0-4.8 2.4 2.4 0 0 1 0 4.8z" fill="#fff"/></svg>
    <div>Thistle Community Center<br>412 Farrow Lane<br>Portland, ME 04219</div>
  </div>
  <div class="contact contact-phone">
    <svg width="32" height="32" viewBox="0 0 32 32" aria-hidden="true"><circle cx="16" cy="16" r="16" fill="var(--navy)"/><path d="M11.5 8.5l2.6 3.2-1.4 2c.9 2 2.4 3.6 4.4 4.6l2-1.4 3.2 2.6-1.4 2.7c-5.6.3-11-5-11-10.8z" fill="#fff"/></svg>
    <span>207-583-1924</span>
  </div>
  <div class="contact contact-email">
    <svg width="32" height="32" viewBox="0 0 32 32" aria-hidden="true"><circle cx="16" cy="16" r="16" fill="var(--navy)"/><rect x="8.5" y="11" width="15" height="10.5" fill="none" stroke="#fff" stroke-width="1.5"/><path d="M8.5 11l7.5 6 7.5-6M8.5 21.5l5.5-5M23.5 21.5l-5.5-5" fill="none" stroke="#fff" stroke-width="1.5"/></svg>
    <span>contact@vellorbrook.org</span>
  </div>
  <div class="contact contact-web">
    <svg width="32" height="32" viewBox="0 0 32 32" aria-hidden="true"><circle cx="16" cy="16" r="16" fill="var(--navy)"/><g fill="none" stroke="#fff" stroke-width="1.4"><circle cx="16" cy="16" r="8"/><ellipse cx="16" cy="16" rx="3.5" ry="8"/><path d="M8 16h16M9.2 12h13.6M9.2 20h13.6"/></g></svg>
    <span>www.toskin.org</span>
  </div>

  <div class="rule"></div>
</main>
</body>
</html>
```